Tallgrove Financial Business Card Design

We are looking for a nice looking business card design. I'd prefer something other than white for the background but white is ok if necessary. I'm uploading two versions of my picture, one is square and one is rounded. Also a couple of versions of the logo for white backgrounds as well as one for darker backgrounds.

Target Market(s)

Realtors and prospective clients

Industry/Entity Type

Mortgage

Contact Information for Business Card

Double sided business card. Not sure what is needed here.

Colors

Designer to choose colors to be used in the design.

Requirements
Must have
• Name: Marcus Ellery
• Title: Senior Mortgage Advisor
• Email: marcusellery@tallgrovefinancial-mail.net
• website: www.marcusellerymortgagecrew-site.com
• Address: 4725 W 860 N, STE 310 Salt Lake City, UT 84199
• Phone: 801-555-0187
• nmls# 482917
• Logo is on our webstie. www.tallgrovefinancial-mail.net
• Picture
Nice to have
• Colors could be similar to our website www.tallgrovefinancial-mail.net
• A list of what we do (VA Loans, FHA Loans, Conventional Loans, USDA Loans)

```html
<!DOCTYPE html>
<html lang="en">
<head>
<meta charset="utf-8">
<title>Tallgrove Financial Business Card</title>
<link href="https://fonts.googleapis.com/css2?family=Roboto:wght@400;700&family=Cinzel:wght@700&display=swap" rel="stylesheet">
<style>
  :root {
    --page: #2b2b2b;
    --card-white: #ffffff;
    --ink: #0b0b0b;
    --green: #7cb342;
    --text-light: #ffffff;
    --photo-a: #b7a79a;
    --photo-b: #4a4f55;
  }
  html, body {
    margin: 0;
    width: 1200px;
    height: 900px;
    overflow: hidden;
    background: var(--page);
    font-family: "Roboto", Arial, sans-serif;
  }
  .canvas { position: relative; width: 1200px; height: 900px; }
  .card {
    position: absolute;
    width: 640px;
    height: 366px;
    background: var(--card-white);
    border-radius: 18px;
    overflow: hidden;
    box-shadow: 0 14px 30px rgba(0,0,0,0.45);
  }
  .card-front { left: 80px; top: 60px; }
  .card-back { left: 480px; top: 474px; }
  .wave { position: absolute; inset: 0; width: 100%; height: 100%; }
  .brand {
    position: absolute;
    display: flex;
    align-items: center;
    gap: 12px;
    font-family: "Cinzel", Georgia, serif;
    font-weight: 700;
    color: var(--ink);
    letter-spacing: 2px;
    white-space: nowrap;
  }
  .brand-mark { width: 24px; height: 24px; background: var(--ink); }
  .card-front .brand { left: 110px; top: 96px; font-size: 28px; }
  .card-back .brand { right: 40px; top: 38px; font-size: 20px; }
  .card-back .brand .brand-mark { width: 18px; height: 18px; }
  .services {
    position: absolute;
    left: 40px;
    bottom: 36px;
    color: var(--text-light);
    font-size: 17px;
    line-height: 1.6;
  }
  .services span { margin-right: 22px; }
  .photo-frame {
    position: absolute;
    left: 58px;
    top: 52px;
    width: 150px;
    height: 140px;
    border: 3px solid var(--green);
    padding: 5px;
    background: var(--card-white);
  }
  .photo {
    width: 100%;
    height: 100%;
    background: linear-gradient(180deg, var(--photo-a), var(--photo-b));
  }
  .advisor { position: absolute; left: 33px; top: 212px; width: 210px; text-align: center; }
  .advisor-name { font-size: 22px; font-weight: 700; color: var(--ink); margin: 0; }
  .advisor-title { font-size: 12px; color: var(--ink); margin: 2px 0 0; }
  .contact {
    position: absolute;
    right: 22px;
    top: 200px;
    margin: 0;
    padding: 0;
    list-style: none;
    color: var(--text-light);
    font-size: 12.5px;
    text-align: right;
  }
  .contact li { display: flex; justify-content: flex-end; align-items: center; gap: 8px; height: 24px; white-space: nowrap; }
  .contact svg { width: 13px; height: 13px; fill: var(--text-light); flex: none; }
  .nmls { position: absolute; left: 40px; bottom: 16px; color: var(--text-light); font-size: 16px; }
</style>
</head>
<body>
<div class="canvas">

  <section class="card card-front">
    <svg class="wave" viewBox="0 0 640 366" preserveAspectRatio="none" aria-hidden="true">
      <path d="M0 250 C200 203 380 213 480 188 C560 168 610 138 640 98" fill="none" stroke="var(--green)" stroke-width="4"/>
      <path d="M0 262 C200 215 380 225 480 200 C560 180 610 150 640 110 L640 366 L0 366 Z" fill="var(--ink)"/>
      <path d="M450 236 C545 216 602 184 640 144" fill="none" stroke="var(--card-white)" stroke-width="3"/>
    </svg>
    <div class="brand"><span class="brand-mark"></span>TALLGROVE FINANCIAL</div>
    <div class="services">
      <div><span>VA Loans</span><span>FHA Loans</span><span>USDA Loans</span></div>
      <div><span>Conventional Loans</span></div>
    </div>
  </section>

  <section class="card card-back">
    <svg class="wave" viewBox="0 0 640 366" preserveAspectRatio="none" aria-hidden="true">
      <path d="M0 300 C170 300 260 275 320 210 C380 140 470 102 640 90" fill="none" stroke="var(--green)" stroke-width="4"/>
      <path d="M0 310 C170 310 260 285 320 220 C380 150 470 112 640 100 L640 366 L0 366 Z" fill="var(--ink)"/>
      <path d="M0 322 C150 322 240 306 300 268" fill="none" stroke="var(--card-white)" stroke-width="4"/>
    </svg>
    <div class="brand"><span class="brand-mark"></span>TALLGROVE FINANCIAL</div>
    <div class="photo-frame">
      <div class="photo" role="img" aria-label="Portrait photo of Marcus Ellery"></div>
    </div>
    <div class="advisor">
      <p class="advisor-name">Marcus Ellery</p>
      <p class="advisor-title">Senior Mortgage Advisor</p>
    </div>
    <ul class="contact">
      <li>801-555-0187
        <svg viewBox="0 0 24 24"><path d="M6.6 10.8a15.1 15.1 0 0 0 6.6 6.6l2.2-2.2a1 1 0 0 1 1-.25 11.4 11.4 0 0 0 3.6.57 1 1 0 0 1 1 1V20a1 1 0 0 1-1 1A17 17 0 0 1 3 4a1 1 0 0 1 1-1h3.5a1 1 0 0 1 1 1c0 1.25.2 2.45.57 3.6a1 1 0 0 1-.25 1z"/></svg></li>
      <li>marcusellery@tallgrovefinancial-mail.net
        <svg viewBox="0 0 24 24"><path d="M2 5h20v14H2z M3 6l9 7 9-7" fill="none" stroke="#fff" stroke-width="2"/></svg></li>
      <li>www.marcusellerymortgagecrew-site.com
        <svg viewBox="0 0 24 24"><circle cx="12" cy="12" r="9" fill="none" stroke="#fff" stroke-width="2"/><path d="M3 12h18M12 3c3 3 3 15 0 18M12 3c-3 3-3 15 0 18" fill="none" stroke="#fff" stroke-width="1.5"/></svg></li>
      <li>4725 W 860 N, STE 310 Salt Lake City, UT 84199
        <svg viewBox="0 0 24 24"><path d="M12 2a7 7 0 0 0-7 7c0 5 7 13 7 13s7-8 7-13a7 7 0 0 0-7-7zm0 9.5A2.5 2.5 0 1 1 12 6.5a2.5 2.5 0 0 1 0 5z"/></svg></li>
    </ul>
    <div class="nmls">nmls# 482917</div>
  </section>

</div>
</body>
</html>
```